Landing page for a cyber security service provider called 'Lumen Grove'

The client is a new cyber security company in need of a website landing page at lumengrove.example.

Their visual identity is modern, playful, clean and uncluttered and represents innovation, connectivity and approachability.

The company logo is provided in black (attached) but the client is open to changing the colour to align with the new website design.

The landing page needs to contain:
- A call to action with a 'Get Started' button
-Links to blank 'How it works', 'Products', 'Pricing', 'About Us' and 'Contact Us' pages (that we'll fill out later)

Target Market(s)

Medium to large businesses who probably don't understand cyber / cyber security but need their business to be protected.

Industry/Entity Type

Cyber Security

Coding

Coded - Design and coding required

Number of Pages Required

1 page

Font styles to use
Sans Serif
Other font styles liked:
• Helvetica

Requirements
Nice to have
• Hero banner at the top of the landing page.
Should not have
• Should not look like a traditional cyber / cyber security design (eg no dark blue/ black, red/black colour combinations). Please no military styles (eg no shields, cannons, swords, guns)

```html
<!DOCTYPE html>
<html lang="en">
<head>
<meta charset="utf-8">
<title>Lumen Grove — Cybersecurity Solutions</title>
<link rel="stylesheet" href="https://fonts.googleapis.com/css2?family=Poppins:wght@300;700&family=Inter:wght@400;600&display=swap">
<style>
  :root {
    --ink: #2b2a33;
    --paper: #ffffff;
    --sky-top: #5d5a6e;
    --sky-mid: #6f6a78;
    --horizon: #a08d68;
    --glow: rgba(230, 196, 120, 0.55);
    --ridge: #3e3a44;
    --ridge-deep: #34313a;
    --footer: #2b2a33;
  }
  * { margin: 0; padding: 0; box-sizing: border-box; }
  html, body { width: 1200px; height: 648px; overflow: hidden; background: var(--paper); }
  body { position: relative; font-family: "Inter", Helvetica, Arial, sans-serif; color: var(--ink); }

  .site-header { position: absolute; top: 0; left: 0; width: 1200px; height: 85px; background: var(--paper); }
  .brand { position: absolute; left: 141px; top: 30px; font-family: "Poppins", sans-serif; font-weight: 700; font-size: 20px; line-height: 26px; color: var(--ink); text-decoration: none; display: flex; align-items: center; gap: 8px; }
  .brand-dot { width: 12px; height: 12px; border-radius: 50%; background: var(--ink); }
  .main-nav a { position: absolute; top: 34px; font-size: 13px; line-height: 16px; color: var(--ink); text-decoration: none; white-space: nowrap; }
  .main-nav a.is-current { font-weight: 600; }
  .btn { display: flex; align-items: center; justify-content: center; gap: 7px; border-radius: 22px; font-size: 13px; letter-spacing: 0.2px; text-decoration: none; white-space: nowrap; }
  .btn svg { width: 18px; height: 12px; }
  .btn-dark { position: absolute; left: 896px; top: 21px; width: 163px; height: 43px; background: var(--ink); color: var(--paper); }

  .hero { position: absolute; top: 85px; left: 0; width: 1200px; height: 529px; overflow: hidden; }
  .hero-backdrop { position: absolute; inset: 0;
    background:
      radial-gradient(ellipse 300px 40px at 800px 430px, var(--glow), transparent 75%),
      linear-gradient(180deg, var(--sky-top) 0%, var(--sky-mid) 48%, var(--horizon) 74%, var(--ridge) 84%, var(--ridge-deep) 100%); }
  .hero-copy { position: absolute; top: 0; left: 0; width: 1200px; text-align: center; color: var(--paper); }
  .hero-title { font-family: "Poppins", sans-serif; font-size: 45px; line-height: 52px; padding-top: 152px; }
  .hero-title .strong { display: block; font-weight: 700; }
  .hero-title .light { display: block; font-weight: 300; }
  .hero-lede { margin: 12px auto 0; width: 640px; font-size: 14px; line-height: 27px; }
  .btn-light { position: absolute; left: 520px; top: 333px; width: 161px; height: 42px; background: var(--paper); color: var(--ink); }

  .site-footer { position: absolute; top: 614px; left: 0; width: 1200px; height: 34px; background: var(--footer); color: var(--paper); font-size: 12.5px; display: flex; align-items: center; justify-content: center; }
</style>
</head>
<body>
  <header class="site-header">
    <a class="brand" href="#"><span class="brand-dot"></span>Lumen Grove</a>
    <nav class="main-nav">
      <a class="is-current" href="#" style="left:362px">Home</a>
      <a href="#" style="left:434px">How it works</a>
      <a href="#" style="left:540px">About Us</a>
      <a href="#" style="left:625px">Products</a>
      <a href="#" style="left:712px">Pricing</a>
      <a href="#" style="left:784px">Contact us</a>
    </nav>
    <a class="btn btn-dark" href="#">GET STARTED
      <svg viewBox="0 0 18 12" fill="none" stroke="currentColor" stroke-width="2"><path d="M0 6h16M11 1l5 5-5 5"/></svg>
    </a>
  </header>

  <section class="hero">
    <div class="hero-backdrop" role="img" aria-label="Starry night sky above mountain peaks with a warm glow on the horizon"></div>
    <div class="hero-copy">
      <h1 class="hero-title"><span class="strong">CYBERSECURITY SOLUTIONS</span><span class="light">FOR YOUR BUSINESS</span></h1>
      <p class="hero-lede">Protect your people, network, devices, and data from internal and external threats with Lumen Grove IT security solutions.</p>
    </div>
    <a class="btn btn-light" href="#">GET STARTED
      <svg viewBox="0 0 18 12" fill="none" stroke="currentColor" stroke-width="2"><path d="M0 6h16M11 1l5 5-5 5"/></svg>
    </a>
  </section>

  <footer class="site-footer">© 2024 LUMEN GROVE PREVENT PROTECT RESPOND. ALL RIGHTS RESERVED</footer>
</body>
</html>
```